Need a cover for eBook:
Title is: 41 Blunders That Sink Your Indie-Released Volume.
Remarks about the title: I know that is difficult to design a cover with a number. You can add the word TOP (in caps or not) before 41 blunders. It is not mandatory to insert the word TOP. It is up to you if you think you can create a better cover.
Subtitle is: A Newcomer's Manual for Releasing Solo, Arranging Pictures and Words, Planning Pages, Boosting Sign-ups and Moving More Copies
Author: Dennis R. Walbrey
Publisher: Quillmark Press
The book made the presentation of errors that can occur during the production of an ebook. Title must be big, the title should be readable even when the image is reduced in size. No photo please.
I join my projects as an example. Do what you want but I need impact.

Target Market(s)

Book to sell first at Brimfold Reader Shop. Target is authors, men or women, who want to produce ebooks.

Industry/Entity Type

Publishing Company

Font styles to use
Sans Serif

Colors
3176b5
9bcb3c

Requirements
Must have
• High readability when cover is small.
• Here is the definition of the word KILL
• put an end to or cause the failure or defeat of (something).
• "the committee voted to kill the project"
• synonyms: destroy, put an end to, end, extinguish, dash, quash, ruin, wreck, shatter, smash, crush, scotch, thwart; informalput the kibosh on, stymie, scuttle
• "this would kill all hopes of progress"
• veto, defeat, vote down, rule against, reject, throw out, overrule, overturn, put a stop to, quash, squash
• "an opposition attempt to kill the bill"
Nice to have
• I suggested 2 colors but you can you use another one or two. I want cover that sell. There is so bright ideas here. Come on down!
Should not have
• No picture or photo. If a photo or an object had power to the cover, you can insert one. I don't want a photo-collage.

```html
<!DOCTYPE html>
<html lang="en">
<head>
<meta charset="utf-8">
<title>41 Blunders That Sink Your Indie-Released Volume</title>
<link rel="stylesheet" href="https://fonts.googleapis.com/css2?family=Fira+Sans+Condensed:wght@500;600;700&family=Saira+Condensed:wght@600;700&display=swap">
<style>
  :root {
    --sky-blue: #1f6fae;
    --night: #000000;
    --lime: #9be60f;
    --orange: #f26a1b;
    --white: #ffffff;
  }
  html, body {
    margin: 0;
    padding: 0;
    width: 750px;
    height: 1200px;
    overflow: hidden;
    background: var(--night);
  }
  .cover {
    position: relative;
    width: 750px;
    height: 1200px;
    overflow: hidden;
    background: var(--night);
    font-family: "Fira Sans Condensed", sans-serif;
  }
  .sky {
    position: absolute;
    left: 0;
    top: 0;
    width: 750px;
    height: 760px;
    background: var(--sky-blue);
  }
  .scene-art {
    position: absolute;
    left: 0;
    top: 80px;
    width: 330px;
    height: 680px;
    background: linear-gradient(to right, #050a10 0%, #0c2a44 55%, rgba(31,111,174,0) 100%);
  }
  .author {
    position: absolute;
    top: 22px;
    left: 0;
    width: 750px;
    text-align: center;
    margin: 0;
    font-weight: 700;
    font-size: 44px;
    letter-spacing: 0.5px;
    color: var(--white);
  }
  .author .first-name { color: var(--orange); }
  .title { margin: 0; }
  .title-number {
    position: absolute;
    left: 300px;
    top: 255px;
    width: 505px;
    text-align: center;
    font-family: "Saira Condensed", sans-serif;
    font-weight: 700;
    font-size: 360px;
    line-height: 300px;
    color: var(--lime);
  }
  .title-word {
    position: absolute;
    left: 300px;
    top: 548px;
    width: 505px;
    text-align: center;
    font-family: "Saira Condensed", sans-serif;
    font-weight: 700;
    font-size: 104px;
    line-height: 100px;
    color: var(--white);
  }
  .title-rest {
    position: absolute;
    left: 0;
    top: 782px;
    width: 750px;
    text-align: center;
    font-weight: 700;
    font-size: 60px;
    line-height: 68px;
    color: var(--lime);
  }
  .subtitle {
    position: absolute;
    left: 0;
    top: 928px;
    width: 750px;
    margin: 0;
    text-align: center;
    font-weight: 600;
    font-size: 23px;
    line-height: 32px;
    color: var(--white);
  }
  .publisher {
    position: absolute;
    left: 0;
    top: 1098px;
    width: 750px;
    margin: 0;
    text-align: center;
    font-weight: 700;
    font-size: 46px;
    color: var(--orange);
  }
</style>
</head>
<body>
  <main class="cover">
    <div class="sky"></div>
    <div class="scene-art" role="img" aria-label="Silhouette of a bare tree with a person sitting against its trunk"></div>

    <p class="author"><span class="first-name">Dennis</span> R. Walbrey</p>

    <h1 class="title">
      <span class="title-number">41</span>
      <span class="title-word">BLUNDERS</span>
      <span class="title-rest">THAT SINK YOUR INDIE-<br>RELEASED VOLUME</span>
    </h1>

    <p class="subtitle">A Newcomer's Manual for Releasing Solo,<br>Arranging Pictures and Words, Planning Pages,<br>Boosting Sign-ups and Moving More Copies</p>

    <p class="publisher">Quillmark Press</p>
  </main>
</body>
</html>
```